We want a business card/punch card for our business. We are including examples of our current business card (we like the front of our business card and not looking to remake it). We need only back side to be designed in form of a punch card (we are including a sample of the punch card we made, but are unsatisfied). For each $180 spend (9 punches) our clients have $20 off.

Colors
886aae

```html
<!DOCTYPE html>
<html lang="en">
<head>
<meta charset="utf-8">
<title>Lotus Path Studio – Business Card and Punch Card</title>
<link rel="stylesheet" href="https://fonts.googleapis.com/css2?family=Open+Sans:wght@400;600&family=Roboto:wght@300;400&display=swap">
<style>
  :root {
    --page: #ececef;
    --purple: #5b2b93;
    --purple-soft: #886aae;
    --blue: #5667b9;
    --blue-mid: #6f7fcc;
    --lavender: #b9c1ec;
    --lavender-light: #d6dbf5;
    --logo-ink: #4a4fae;
    --ring: #6e74cf;
    --white: #ffffff;
  }
  * { box-sizing: border-box; margin: 0; padding: 0; }
  html, body {
    width: 1154px; height: 1200px; overflow: hidden;
    background: var(--page);
    font-family: "Open Sans", sans-serif;
  }
  .canvas { position: relative; width: 1154px; height: 1200px; }

  /* ---------- Front card ---------- */
  .card-front {
    position: absolute; left: 30px; top: 40px;
    width: 600px; height: 343px;
    border-radius: 18px; overflow: hidden;
    box-shadow: 0 4px 12px rgba(0,0,0,.18);
  }
  .card-front .background { position: absolute; inset: 0; }
  .pattern-area {
    position: absolute; left: 0; top: 0; width: 330px; height: 343px;
    background: radial-gradient(circle at 45% 45%, var(--lavender-light) 0%, var(--lavender) 75%);
    opacity: .9;
  }
  .brand {
    position: absolute; left: 30px; top: 216px;
    display: flex; align-items: center; gap: 9px;
    font-family: "Open Sans", sans-serif; font-weight: 600;
    font-size: 26px; color: var(--logo-ink); white-space: nowrap;
  }
  .brand-dot {
    width: 20px; height: 20px; border-radius: 50%;
    background: var(--logo-ink);
  }
  .contact {
    position: absolute; right: 34px; color: var(--white);
    font-family: "Roboto", sans-serif; text-align: right;
  }
  .contact-name { top: 34px; }
  .contact-name .name { font-size: 27px; font-weight: 400; }
  .contact-name .phone { font-size: 23px; font-weight: 300; margin-top: 2px; }
  .contact-web { top: 178px; font-size: 17px; font-weight: 300; line-height: 1.45; }
  .contact-social { top: 262px; font-size: 17px; font-weight: 300; line-height: 1.45; }

  /* ---------- Back card (punch card) ---------- */
  .card-back {
    position: absolute; left: 664px; top: 360px;
    width: 460px; height: 805px;
    border-radius: 18px; overflow: hidden;
    background: var(--purple);
    box-shadow: 0 4px 12px rgba(0,0,0,.2);
    color: var(--white);
  }
  .card-frame {
    position: absolute; inset: 16px;
    border: 1px dotted rgba(255,255,255,.55);
  }
  .punch-grid {
    position: absolute; left: 30px; top: 30px; width: 400px;
    display: grid; grid-template-columns: repeat(3, 1fr);
    row-gap: 34px; justify-items: center;
  }
  .punch-spot {
    width: 120px; height: 120px; border-radius: 50%;
    background: radial-gradient(circle, var(--white) 0 40%, var(--blue-mid) 41% 70%, var(--ring) 71% 100%);
    box-shadow: 0 0 0 3px rgba(136,106,174,.55);
  }
  .rule {
    position: absolute; left: 16px; right: 16px;
    border-top: 1px dotted rgba(255,255,255,.6);
  }
  .rule-top { top: 474px; }
  .rule-mid { top: 646px; }
  .message {
    position: absolute; left: 30px; right: 30px; top: 494px;
    text-align: center; font-size: 17px; line-height: 1.3;
  }
  .services {
    position: absolute; left: 24px; right: 24px; top: 656px;
    font-family: "Roboto", sans-serif; font-weight: 300;
    font-size: 21px; text-align: center; line-height: 1.4;
    white-space: nowrap;
  }
  .services p { border-bottom: 1px dotted rgba(255,255,255,.5); }
  .services p:last-child { border-bottom: 0; }
  .sep {
    display: inline-block; width: 8px; height: 8px;
    border: 2px solid var(--white); border-radius: 50%;
    margin: 0 6px; vertical-align: middle;
  }
</style>
</head>
<body>
<main class="canvas">

  <section class="card-front" aria-label="Business card front">
    <svg class="background" viewBox="0 0 600 343" preserveAspectRatio="none" aria-hidden="true">
      <rect width="600" height="343" fill="var(--lavender)"/>
      <path d="M345,0 C285,110 300,250 372,343 L600,343 L600,0 Z" fill="var(--blue-mid)"/>
      <path d="M362,0 C305,110 322,250 392,343 L600,343 L600,0 Z" fill="var(--blue)"/>
      <path d="M395,0 C350,70 372,125 420,150 C470,130 540,118 600,122 L600,0 Z" fill="var(--purple)"/>
      <path d="M420,150 C470,130 540,118 600,122 L600,128 C540,124 480,136 428,156 Z" fill="var(--purple-soft)"/>
    </svg>
    <div class="pattern-area" role="img" aria-label="Soft lavender mandala pattern with a lotus emblem"></div>
    <div class="brand"><span class="brand-dot"></span>Lotus Path Studio</div>
    <div class="contact contact-name">
      <p class="name">Selene Marwood</p>
      <p class="phone">555-210-4738</p>
    </div>
    <div class="contact contact-web">
      <p>www.lotuspathstudio.com</p>
      <p>hello@lotuspathstudio.com</p>
    </div>
    <div class="contact contact-social">
      <p>lotuspathstudio.com/events</p>
      <p>lotuspathstudio.com/circles</p>
    </div>
  </section>

  <section class="card-back" aria-label="Punch card back">
    <div class="card-frame"></div>
    <div class="punch-grid">
      <div class="punch-spot" role="img" aria-label="Mandala punch spot 1"></div>
      <div class="punch-spot" role="img" aria-label="Mandala punch spot 2"></div>
      <div class="punch-spot" role="img" aria-label="Mandala punch spot 3"></div>
      <div class="punch-spot" role="img" aria-label="Mandala punch spot 4"></div>
      <div class="punch-spot" role="img" aria-label="Mandala punch spot 5"></div>
      <div class="punch-spot" role="img" aria-label="Mandala punch spot 6"></div>
      <div class="punch-spot" role="img" aria-label="Mandala punch spot 7"></div>
      <div class="punch-spot" role="img" aria-label="Mandala punch spot 8"></div>
      <div class="punch-spot" role="img" aria-label="Mandala punch spot 9"></div>
    </div>
    <div class="rule rule-top"></div>
    <p class="message">This card is a symbol of appreciation from us to you. Without your business, we would not be able to do what we love most!<br>When you fill out this card, you will receive $20 towards your next Weekly Event, Workshop, or Private Session.</p>
    <div class="rule rule-mid"></div>
    <div class="services">
      <p>Tantra<span class="sep"></span>Tao<span class="sep"></span>Yoga<span class="sep"></span>Tai Chi<span class="sep"></span>Reiki</p>
      <p>Sacred Sexuality<span class="sep"></span>Sexual Healing</p>
      <p>Sound Healing<span class="sep"></span>Energy Work<span class="sep"></span>Rituals</p>
      <p>Partners Yoga<span class="sep"></span>Four Hands Massage</p>
    </div>
  </section>

</main>
</body>
</html>
```